Web Design Project

The aim of this project to design a website for a service that would offer services for small business and non profit organizations using opensource software that is weaved to work together in harmony.

The website name is: velitra.net

Velitra in Arabic means: cabbage. Cabbage is composed of leaves, actually there is nothing except leaves. Each leave by itself is not called cabbage, but a collection of leaves that are organized in a central way would give us cabbage.

Same idea for Velitra where open source software very well organized and integrated would create a new thing with a new value.
Updates

Target Market(s)

Small business, Europe, Africa, Far east and Middle east

Industry/Entity Type

Small Business

Requirements
Must have
• The website would offer the following sections:
* Home page
* Benefits: value of velitra
* Applications: applications offered by velitra
* Pricing
* Purchase
* Customer log in
* Support
- FAQ
- Knowledge base
- Forums
- Open tickets

Please take the following consideration in design:
* White should predominate
* Only black and the colors of logo are permitted (attched)
Nice to have
• Design is better to express:
* Openness
* Dynamic
* Usable
* Cost effective

Files

```html
<!DOCTYPE html>
<html lang="en">
<head>
<meta charset="utf-8">
<title>Velitra — Home</title>
<link href="https://fonts.googleapis.com/css2?family=Open+Sans:wght@300;400;600;700&display=swap" rel="stylesheet">
<style>
  :root{
    --white:#ffffff;
    --ink:#111111;
    --blue:#1a8fd6;
    --green:#7ac142;
    --panel:#f2f2f2;
    --field:#eeeeee;
    --muted:#666666;
    --footer:#555555;
    --cal:#2e2f33;
    --cal-head:#24252a;
    --line:#c8c8c8;
  }
  *{box-sizing:border-box;margin:0;padding:0}
  html,body{width:862px;height:1200px;overflow:hidden;background:var(--white)}
  body{position:relative;font-family:"Open Sans",Arial,sans-serif;color:var(--ink)}

  .site-header{position:absolute;left:0;top:0;width:862px;height:40px;background:var(--white)}
  .brand{position:absolute;left:14px;top:6px;display:flex;align-items:center;gap:8px}
  .brand-dot{width:26px;height:26px;border-radius:50%;background:var(--green)}
  .brand-name{font-size:28px;font-weight:400;color:var(--ink);letter-spacing:.5px;line-height:28px}
  .main-nav a{position:absolute;top:13px;font-size:12px;color:var(--ink);text-decoration:none;transform:translateX(-50%);white-space:nowrap}
  .main-nav .current::after{content:"";position:absolute;left:50%;transform:translateX(-50%);top:15px;width:79px;height:5px;background:var(--green)}

  .hero{position:absolute;left:0;top:40px;width:862px;height:276px;
    background:linear-gradient(100deg,#e9ecef 0%,#c9ccd0 22%,#8a8f96 45%,#5b6068 65%,#c4c7cb 85%,#eef0f2 100%)}
  .hero-title{position:absolute;left:98px;top:122px;font-size:40px;font-weight:300;color:var(--white);letter-spacing:.5px}
  .login{position:absolute;left:668px;top:92px;width:156px;height:171px;background:var(--white);border-radius:3px;box-shadow:0 1px 4px rgba(0,0,0,.25)}
  .login-title{position:absolute;left:0;width:100%;top:17px;text-align:center;font-size:9.5px;font-weight:600}
  .login-fields{position:absolute;left:10px;top:50px;width:136px;height:46px;background:var(--field)}
  .login-fields .label{position:absolute;left:8px;top:5px;font-size:7.5px;color:var(--muted)}
  .login-fields .rule{position:absolute;left:0;right:0;top:22px;height:1px;background:#d8d8d8}
  .login-fields .pass{position:absolute;left:8px;top:25px;font-size:10px;letter-spacing:1px;color:var(--ink)}
  .login-button{position:absolute;left:10px;top:111px;width:136px;height:24px;background:var(--green);color:var(--white);font-size:9px;font-weight:600;text-align:center;line-height:24px}
  .remember{position:absolute;left:10px;top:144px;font-size:7.5px;color:#444;display:flex;align-items:center;gap:6px}
  .remember .box{width:7px;height:7px;border:1px solid #ccc;background:#f6f6f6}
  .forgot{position:absolute;right:8px;top:144px;font-size:7.5px;color:#444}

  .welcome{position:absolute;left:47px;top:337px;width:770px;height:351px;background:var(--panel)}
  .welcome h1{margin-top:18px;text-align:center;font-size:20px;font-weight:400;color:var(--blue)}
  .welcome p{margin:10px 13px 0 25px;font-size:11.6px;line-height:16px;text-indent:66px}
  .welcome h1 + p{margin-top:12px}

  .feeds{position:absolute;left:49px;top:712px;width:772px;height:266px;background:var(--panel)}
  .feeds h2{position:absolute;top:26px;font-size:17px;font-weight:400;color:var(--blue);transform:translateX(-50%);white-space:nowrap}
  .feeds .divider{position:absolute;left:370px;top:26px;width:1px;height:210px;background:var(--line)}
  .news-box{position:absolute;left:45px;top:69px;width:292px;height:162px;background:var(--white)}
  .news-box p{margin:14px 30px 0 5px;font-size:11.6px;line-height:16.5px}
  .news-box p + p{margin-top:12px}
  .scroll{position:absolute;top:8px;width:5px;background:#bdbdbd;border-radius:2px}
  .scroll .thumb{position:absolute;left:0;top:0;width:5px;background:#2b2b2b;border-radius:2px}
  .events-box{position:absolute;left:397px;top:69px;width:183px;height:162px;background:var(--white)}
  .events-box ul{list-style:none;margin:16px 0 0 10px;font-size:11.6px;line-height:16.5px;color:#222}
  .events-box li + li{margin-top:9px}
  .events-box .date{color:#444}

  .calendar{position:absolute;left:599px;top:69px;width:160px;height:160px;background:var(--cal);border-radius:3px;overflow:hidden}
  .cal-head{height:28px;background:var(--green);color:var(--white);font-size:10px;display:flex;align-items:center;justify-content:space-between;padding:0 10px}
  .cal-days,.cal-grid{display:grid;grid-template-columns:repeat(7,1fr);padding:0 5px;text-align:center}
  .cal-days{background:var(--cal-head);height:19px;line-height:19px;font-size:8.5px;color:#e8e8e8}
  .cal-grid{margin-top:5px;font-size:9px;color:#cfcfcf;grid-auto-rows:19px;line-height:19px}
  .cal-grid .off{color:#808080}
  .cal-grid .today span{display:inline-block;width:17px;height:17px;line-height:17px;background:var(--green);color:var(--white);border-radius:3px}

  .site-footer{position:absolute;left:0;top:1002px;width:862px;height:198px;background:var(--footer);border-radius:5px 5px 0 0;color:var(--white)}
  .site-map{list-style:none;position:absolute;left:45px;top:21px;font-size:11.6px;line-height:20.5px}
  .support-links{list-style:none;position:absolute;left:382px;top:22px;font-size:11.6px;line-height:26px}
  .domain{position:absolute;left:0;width:100%;top:176px;text-align:center;font-size:11.6px}
</style>
</head>
<body>

<header class="site-header">
  <div class="brand"><span class="brand-dot"></span><span class="brand-name">velitra</span></div>
  <nav class="main-nav">
    <a class="current" href="#" style="left:340px">Home</a>
    <a href="#" style="left:428px">Benefits</a>
    <a href="#" style="left:521px">Purchase</a>
    <a href="#" style="left:631px">Applications</a>
    <a href="#" style="left:733px">Benefits</a>
    <a href="#" style="left:818px">Support</a>
  </nav>
</header>

<section class="hero" role="img" aria-label="Photo of a smiling business team standing together in a bright office">
  <div class="hero-title">Unity is Strenght</div>
  <form class="login">
    <div class="login-title">Welcome</div>
    <div class="login-fields">
      <span class="label">Username</span>
      <span class="rule"></span>
      <span class="pass">••••••••</span>
    </div>
    <div class="login-button">Sign in</div>
    <div class="remember"><span class="box"></span>Remember me</div>
    <div class="forgot">I forgot!</div>
  </form>
</section>

<section class="welcome">
  <h1>Welcome to Velitra!</h1>
  <p>Velitra is a International company which offers softwares and solutions to IT sector companies which mainly produce Open Source softwares and offer software and consult soltuions. Velitra is a International company which offers softwares and solutions to IT sector companies which mainly produce Open Source softwares and offer software and consult soltuions.Velitra is a International company which offers softwares and solutions to IT sector companies which mainly produce Open Source softwares and offer software and consult soltuions.</p>
  <p>Velitra is a International company which offers softwares and solutions to IT sector companies which mainly produce Open Source softwares and offer software and consult soltuions. Velitra is a International company which offers softwares and solutions to IT sector companies which mainly produce Open Source softwares and offer software and consult soltuions.Velitra is a International company which offers softwares and solutions to IT sector companies which mainly produce Open Source softwares and offer software and consult soltuions.</p>
  <p>Velitra is a International company which offers softwares and solutions to IT sector companies which mainly produce Open Source softwares and offer software and consult soltuions. Velitra is a International company which offers softwares and solutions to IT sector companies which mainly produce Open Source softwares and offer software and consult soltuions.Velitra is a International company which offers softwares and solutions to IT sector companies which mainly produce Open Source softwares and offer software and consult soltuions.</p>
</section>

<section class="feeds">
  <h2 style="left:179px">News</h2>
  <div class="divider"></div>
  <h2 style="left:595px">Events Calender</h2>

  <div class="news-box">
    <p>Today CEO has just annouced the Academic Status and turnover which was boosted to peaks from it basic.</p>
    <p>Today CEO has just annouced the Academic Status and turnover which was boosted to peaks from it basic.</p>
    <div class="scroll" style="left:282px;height:134px"><div class="thumb" style="height:48px"></div></div>
  </div>

  <div class="events-box">
    <ul>
      <li><div class="date">9-Apri-2013</div><div>&gt; Company Inaguration Day</div></li>
      <li><div class="date">9-Apri-2013</div><div>&gt; Company Inaguration Day</div></li>
      <li><div class="date">9-Apri-2013</div><div>&gt; Company Inaguration Day</div></li>
    </ul>
    <div class="scroll" style="left:172px;height:138px"><div class="thumb" style="height:52px"></div></div>
  </div>

  <div class="calendar">
    <div class="cal-head">
      <svg width="9" height="10" viewBox="0 0 9 10"><path d="M8 0 L0 5 L8 10 Z" fill="#fff"/></svg>
      <span>April 2013</span>
      <svg width="9" height="10" viewBox="0 0 9 10"><path d="M1 0 L9 5 L1 10 Z" fill="#fff"/></svg>
    </div>
    <div class="cal-days"><span>Sun</span><span>Mon</span><span>Tue</span><span>Wed</span><span>Thu</span><span>Fri</span><span>Sat</span></div>
    <div class="cal-grid">
      <span class="off">31</span><span>1</span><span>2</span><span>3</span><span>4</span><span>5</span><span>6</span>
      <span>7</span><span>8</span><span class="today"><span>9</span></span><span>10</span><span>11</span><span>12</span><span>13</span>
      <span>14</span><span>15</span><span>16</span><span>17</span><span>18</span><span>19</span><span>20</span>
      <span>21</span><span>22</span><span>23</span><span>24</span><span>25</span><span>26</span><span>27</span>
      <span>28</span><span>29</span><span>30</span><span class="off">1</span><span class="off">2</span><span class="off">3</span><span class="off">4</span>
    </div>
  </div>
</section>

<footer class="site-footer">
  <ul class="site-map">
    <li>* Home page</li>
    <li>* Benefits: value of velitra</li>
    <li>* Applications: applications offered by velitra</li>
    <li>* Pricing</li>
    <li>* Purchase</li>
    <li>* Customer log in</li>
    <li>* Support</li>
  </ul>
  <ul class="support-links">
    <li>- FAQ</li>
    <li>- Knowledge base</li>
    <li>- Forums</li>
    <li>- Open tickets</li>
  </ul>
  <div class="domain">www.velitra.net</div>
</footer>

</body>
</html>
```